PLEASE READ - DESIGN for Music Cover Tunevault - DJ and Female Singer

A nice cover to be put on Tunevault.
Definitely will be on Tunevault and All Media
Name of the song: Marivella
Singer name: Tara Wolskind
DJ name: DJ Roland Kestry

Marivella definition: A desire to be in the Sun

We need eye catching icon or something that can attract people's eyes when they see it immediately. Design must be elegant. This is not some type of Club Banging Music. The singer is a romantic and sophisticated audiophile jazz acoustic recording artist. DJ is not playing in some clubs but exclusive.

Photo of singer and DJ can be on the cover OR just photo of the singer OR just an Icon wifh their names and the song name.

Avoid these colors: Pink, Purple, Silver !!
For the background color try: A mixed of Black or Gold with Elegant Yellow, Pastel Orange, or light Blue.
For name of the song and Icon color : can be of Gold or even Red or White.
Or you can try and mix it all up yourself

Icon ideas: can be a combination of letter Capital C with small B & Capital V alone or mixed with a sun logo or half of Sun. Some cool stuff.
CB is Tara Wolskind
V is for the DJ name

Target Market(s)

Young Adult, Lounge Crowd, Club Goers / Lounge Goers, Ladies, Executives, Adults, Music Industry

Industry/Entity Type

Entertainment Industry

Font styles to use
Serif

Requirements
Must have
• MARIVELLA ( song name )
• Available on Tunevault logo
• EYE CATCHING ICON or LOGO
Should not have
• Avoid this color :
• Pink, Purple, Silver, White
• Our first project was already consisting these colors, we will attach the old design of the first song but PLEASE DO NOT apply the older design to this new project :)

```html
<!DOCTYPE html>
<html lang="en">
<head>
<meta charset="utf-8">
<title>Marivella – Disc Label</title>
<link rel="stylesheet" href="https://fonts.googleapis.com/css2?family=Monoton&family=Open+Sans:wght@400;600;700&display=swap">
<style>
  :root {
    --backdrop: #ece7df;
    --disc-black: #050505;
    --title-orange: #f39a1e;
    --label-white: #f2f2f2;
    --singer-cyan: #4fc3e8;
    --dj-red: #e0261b;
    --project-orange: #f2a21c;
    --genre-green: #5fae2e;
    --art-red: #e2321a;
    --art-orange: #f07a1c;
    --art-yellow: #f5c21a;
    --photo-warm: #c9a27a;
    --photo-deep: #4a2a22;
    --hub-light: #b9b4ab;
    --hub-dark: #6e6a63;
    --badge-border: #8a8a8a;
  }
  html, body {
    margin: 0;
    padding: 0;
    width: 1200px;
    height: 720px;
    overflow: hidden;
    background: var(--backdrop);
  }
  .canvas {
    position: relative;
    width: 1200px;
    height: 720px;
  }
  .disc {
    position: absolute;
    left: 278px;
    top: 38px;
    width: 644px;
    height: 644px;
  }
  .disc-title {
    font-family: "Monoton", "Open Sans", sans-serif;
    font-size: 44px;
    fill: var(--title-orange);
    letter-spacing: 2px;
  }
  .credit {
    font-family: "Open Sans", Arial, sans-serif;
    font-size: 11.5px;
  }
  .credit-label { font-weight: 700; fill: var(--label-white); }
  .credit-singer { fill: var(--singer-cyan); }
  .credit-dj { fill: var(--dj-red); }
  .credit-project { fill: var(--project-orange); }
  .credit-genre { fill: var(--genre-green); }
  .artist-mark {
    font-family: "Open Sans", Arial, sans-serif;
    font-weight: 700;
    font-size: 40px;
    fill: var(--dj-red);
  }
  .store-badge-text {
    font-family: "Open Sans", Arial, sans-serif;
    font-weight: 600;
    fill: var(--label-white);
  }
</style>
</head>
<body>
<main class="canvas">
  <svg class="disc" viewBox="0 0 644 644" xmlns="http://www.w3.org/2000/svg" aria-label="Marivella disc label">
    <defs>
      <clipPath id="disc-shape">
        <circle cx="322" cy="322" r="322"/>
      </clipPath>
      <linearGradient id="artwork-fill" x1="0" y1="0" x2="1" y2="1">
        <stop offset="0" stop-color="var(--art-red)"/>
        <stop offset="0.55" stop-color="var(--art-orange)"/>
        <stop offset="1" stop-color="var(--art-yellow)"/>
      </linearGradient>
      <linearGradient id="portrait-fill" x1="0" y1="0" x2="1" y2="1">
        <stop offset="0" stop-color="var(--photo-deep)"/>
        <stop offset="0.5" stop-color="var(--photo-warm)"/>
        <stop offset="1" stop-color="#8a5a2a"/>
      </linearGradient>
      <radialGradient id="hub-fill" cx="0.4" cy="0.4" r="0.7">
        <stop offset="0" stop-color="var(--hub-light)"/>
        <stop offset="1" stop-color="var(--hub-dark)"/>
      </radialGradient>
    </defs>

    <g clip-path="url(#disc-shape)">
      <rect class="disc-base" width="644" height="644" fill="var(--disc-black)"/>

      <path class="disc-artwork" role="img" aria-label="Colourful red and orange decorative pattern artwork"
            d="M0 230 Q80 190 170 225 Q230 250 220 330 Q250 390 320 420 Q390 470 380 560 L360 644 L0 644 Z"
            fill="url(#artwork-fill)"/>

      <rect class="disc-portrait" role="img" aria-label="Photo of the singer"
            x="406" y="98" width="260" height="408" fill="url(#portrait-fill)"/>
    </g>

    <text class="disc-title" x="142" y="116">MARIVELLA</text>

    <g class="credits">
      <text class="credit" x="144" y="146"><tspan class="credit-label">Singer name: </tspan><tspan class="credit-singer">Tara Wolskind</tspan></text>
      <text class="credit" x="144" y="165"><tspan class="credit-label">DJ name: </tspan><tspan class="credit-dj">DJ Roland Kestry</tspan></text>
      <text class="credit" x="144" y="184"><tspan class="credit-label">Project: </tspan><tspan class="credit-project">Collaboration</tspan></text>
      <text class="credit" x="144" y="203"><tspan class="credit-label">Genre: </tspan><tspan class="credit-genre">Ibiza Smooth type Lounge Beat</tspan></text>
    </g>

    <g class="disc-hub">
      <circle cx="280" cy="290" r="70" fill="var(--disc-black)"/>
      <circle cx="280" cy="290" r="62" fill="url(#hub-fill)"/>
      <circle cx="280" cy="290" r="24" fill="var(--backdrop)"/>
    </g>

    <text class="artist-mark" x="380" y="462">TW · RK</text>

    <g class="store-badge">
      <rect x="226" y="492" width="168" height="58" rx="9" fill="var(--disc-black)" stroke="var(--badge-border)" stroke-width="1.5"/>
      <circle cx="252" cy="521" r="11" fill="var(--label-white)"/>
      <text class="store-badge-text" x="274" y="514" font-size="12">Available on</text>
      <text class="store-badge-text" x="274" y="538" font-size="22">Tunevault</text>
    </g>
  </svg>
</main>
</body>
</html>
```